Webdesign  Seminare im Bereich persönliche Entwicklung, Spiritualität und Coaching
Webdesign Seminare im Bereich persönliche Entwicklung, Spiritualität und Coaching
Zielgruppe
Wir bieten Seminare im Bereich persönliche Entwicklung, Spiritualität und Coaching an. Unsere Zielgruppe umfasst Menschen zw. 18 und 75 jeglichen Berufsstandes, die sich dafür interessieren ihre tieferen innewohnenden Potenziale kennenzulernen und zu eröffnen.
Dieser Auftrag hier ist ein Teaser-Projekt. Wir wachsen konstant, möchten mehrere Folgeaufträge vergeben und suchen auf diesem Weg einen langfristigen Partner.
Aufgabenstellung
- keine esoterischen Klischee-Bilder, nichts Verspieltes
- unser Auftritt (hier vorerst die Website) soll wärmer wirken als dies aktuell der Fall ist, die Klarheit darf dabei jedoch nicht verloren gehen
- klar, warm, offen, vertraut, seriös
- das Logo darf verändert werden
Aktuell ist recht wenig Bildmaterial vorhanden. Hier wird demnächst nachproduziert. Bitte vorerst, wenn designtechnisch angebracht, Stockmaterial (als Platzhalter) verwenden.

```html
<!DOCTYPE html>
<html lang="de">
<head>
<meta charset="utf-8">
<title>Basisworkshops – Lesen im InnenFeld</title>
<link href="https://fonts.googleapis.com/css2?family=Lato:wght@400;700&family=Montserrat:wght@400;500&display=swap" rel="stylesheet">
<style>
:root{
  --bg:#ecebe6;
  --white:#ffffff;
  --yellow:#fdcf6a;
  --yellow-soft:#fdf3dc;
  --brown:#4a3a14;
  --text:#5a5a5a;
  --dark:#2b2b2b;
  --line:#e6e3dc;
}
*{margin:0;padding:0;box-sizing:border-box}
html,body{width:739px;height:1200px;overflow:hidden;background:var(--bg)}
body{position:relative;font-family:'Lato',sans-serif;color:var(--text)}
.abs{position:absolute}
.site-header{top:0;left:0;width:739px;height:54px;background:var(--white)}
.brand{left:77px;top:11px;display:flex;align-items:center;gap:5px;color:var(--brown);font-family:'Lato',sans-serif;font-weight:700}
.brand-mark{width:9px;height:9px;background:var(--yellow)}
.brand-text{font-size:10px;line-height:12px}
.main-nav{right:74px;top:21px;display:flex;gap:20.5px;font-family:'Montserrat',sans-serif;font-size:7.7px;color:var(--dark)}
.main-nav span{position:relative}
.main-nav .active::after{content:"";position:absolute;left:-4px;right:-3px;bottom:-5px;height:2px;background:var(--yellow)}
.hero{top:54px;left:0;width:739px;height:124px;background:linear-gradient(100deg,#6fa6cf 0%,#a9c7d9 35%,#e6e2d2 65%,#f7e6a6 100%)}
.hero-title{top:108px;left:0;width:739px;text-align:center;font-family:'Montserrat',sans-serif;font-weight:500;font-size:15.5px;letter-spacing:1.2px;color:var(--brown)}
.tabs{top:213px;left:124px;width:493px;height:21px;border-bottom:2px solid var(--yellow);display:flex;justify-content:space-between;font-size:8.3px;color:var(--text)}
.tabs span{padding:0 4px;position:relative}
.tabs .active::after{content:"";position:absolute;left:0;right:0;bottom:-7px;height:2px;background:var(--brown)}
.dates{top:255px;left:77px;width:585px;background:var(--white);border-radius:5px;overflow:hidden}
.dates-head{height:33px;background:var(--yellow);position:relative;font-weight:700;font-size:8.7px;color:var(--brown)}
.row{position:relative;border-bottom:1px solid var(--line);font-size:7.5px;line-height:12.3px}
.row:last-child{border-bottom:none}
.row.hl{background:var(--yellow-soft)}
.cell{position:absolute;top:50%;transform:translateY(-50%)}
.c1{left:23px}.c2{left:142px}.c3{left:228px}.c4{left:396px}
.dates-head .cell{top:50%}
.c4h{left:398px}
.row a{color:var(--text);text-decoration:none;border-bottom:1px solid var(--text)}
.btn{position:absolute;left:519px;top:50%;transform:translateY(-50%);width:46px;height:18px;background:var(--yellow);color:var(--brown);font-family:'Montserrat',sans-serif;font-size:7px;display:flex;align-items:center;justify-content:center}
.copy{left:77px;width:590px;font-size:8.2px;line-height:15.4px}
.copy b{font-weight:700}
.copy a{color:var(--text);text-decoration:none;border-bottom:1px solid var(--text)}
.divider{top:675px;left:77px;width:591px;height:1px;background:#b9b6ad}
.times{top:927px;left:234px;width:270px;background:var(--white);border-radius:5px;overflow:hidden;font-size:7.5px}
.times-head{height:33px;background:var(--yellow);color:var(--brown);font-weight:700;font-size:8.5px;padding:0 16px;display:flex;align-items:center}
.times-row{height:33.5px;display:flex;justify-content:space-between;align-items:center;padding:0 20px 0 16px;border-bottom:1px solid var(--line)}
.times-row:last-child{border-bottom:none}
.social{top:1090px;left:342px;display:flex;gap:8px}
.social span{width:13px;height:13px;border-radius:50%;background:var(--white);display:flex;align-items:center;justify-content:center}
.footer-nav{top:1123px;left:0;width:739px;display:flex;justify-content:center;gap:21px;font-family:'Montserrat',sans-serif;font-size:8px;color:var(--dark)}
.footer-line{top:1156px;left:60px;width:617px;height:1px;background:#8c8a84}
.rights{top:1174px;left:0;width:739px;text-align:center;font-size:5.6px;color:var(--text)}
</style>
</head>
<body>
<header class="abs site-header">
  <div class="abs brand"><span class="brand-mark"></span><span class="brand-text">Lesen im InnenFeld<br>Julius Brandt</span></div>
  <nav class="abs main-nav"><span>Start</span><span>Julius Brandt</span><span>InnenFeld</span><span class="active">Termine</span><span>Blog</span><span>Kontakt</span></nav>
</header>
<div class="abs hero" role="img" aria-label="Weicher Himmel mit Wolken, blau zu warmem Gelb"></div>
<h1 class="abs hero-title">BASISWORKSHOPS</h1>

<div class="abs tabs"><span>Übersicht</span><span class="active">BasisWorkshop</span><span>AufbauWorkshops</span><span>OnlineErlebnisAbend</span><span>LiveMeditationen</span><span>Einzelsitzungen</span></div>

<section class="abs dates">
  <div class="dates-head"><span class="cell c1">Termin</span><span class="cell c2">Ort</span><span class="cell c3">Seminarhaus</span><span class="cell c4h">Preis</span></div>
  <div class="row" style="height:43px"><span class="cell c1">16. – 20.01.2022</span><span class="cell c2">Talheim<br>(Nordhessen)</span><span class="cell c3">Seminarhaus Talblick<br><a>www.seminarhaus-talblick.de</a></span><span class="cell c4">1.290,- €</span><span class="btn">Anmelden</span></div>
  <div class="row" style="height:37px"><span class="cell c1">27. – 31.03.2022</span><span class="cell c2">Talheim<br>(Nordhessen)</span><span class="cell c3">Seminarhaus Talblick<br><a>www.seminarhaus-talblick.de</a></span><span class="cell c4">1.290,- €</span><span class="btn">Anmelden</span></div>
  <div class="row" style="height:50px"><span class="cell c1">25. – 29.04.2022</span><span class="cell c2">Lindau-Nord<br>(Seeland)</span><span class="cell c3">Seminarhaus Morgenlicht<br><a>www.seminarzentrum-</a><br><a>morgenlicht.de</a></span><span class="cell c4">1.390,- €**</span><span class="btn">Anmelden</span></div>
  <div class="row hl" style="height:39px"><span class="cell c1">08. – 12.05.2022</span><span class="cell c2">Talheim<br>(Nordhessen)</span><span class="cell c3">Seminarhaus Talblick<br><a>www.seminarhaus-talblick.de</a></span><span class="cell c4">1.290,- €</span><span class="btn">Anmelden</span></div>
  <div class="row" style="height:45px"><span class="cell c1">16. – 20.05.2022</span><span class="cell c2">Waldhof<br>(Voralpen)</span><span class="cell c3">Seminarhaus Waldsee<br><a>www.seminarhaus-waldsee</a></span><span class="cell c4">1.390,- €**</span><span class="btn">Anmelden</span></div>
</section>

<p class="abs copy" style="top:519px">Alle Preise inkl. gesetzlich gültiger Mehrwertsteuer, bei Präsenzveranstaltungen zuzüglich Unterkunft und Verpflegung, eine Ratenzahlung ist möglich nach Vereinbarung.</p>
<p class="abs copy" style="top:565px">** Der leicht erhöhte Preis ergibt sich aus den deutlich höheren Anreisekosten und -zeiten für unser Team (min. 9 Personen).<br>Wir bitten um euer Verständnis.</p>
<p class="abs copy" style="top:611px"><b>Das Seminarhaus lässt Maskenatteste leider nur ganz bedingt gelten. Mit einem Maskenattest musst du dir für die Wege im Seminarhaus und für das Bedienen am Buffet einen Faceshield mitbringen und aufsetzen.</b></p>

<div class="abs divider"></div>

<p class="abs copy" style="top:694px">Im BasisWorkshop erlernst du den Zugang zum InnenFeld und wie du für dich und andere darin lesen und arbeiten kannst. Anhand unterschiedlicher Übungen erlangst du zum einen Sicherheit im Umgang mit dem Feld, zum anderen heilst du eine Vielzahl an Themen, die dich gerade in deinem Leben hinderlich beeinflussen.</p>
<p class="abs copy" style="top:756px">Nachdem zu Beginn des Workshops alle Teilnehmer ihren Zugang zum InnenFeld geöffnet haben, intensivieren wir die Verbindung durch unterschiedliche Lesungen, die in der Regel paarweise stattfinden und intensiv von mir und meinem Team von sehr erfahrenen Therapeuten begleitet werden. Hierbei betrachtest du unter anderem deine nächsten notwendigen Entwicklungsschritte und du reist mit Hilfe des InnenFeldes zu deinen tief abgespeicherten Blockaden und hemmenden Thematiken und löst diese zügig und nachhaltig auf.</p>
<p class="abs copy" style="top:833px">Übungen zur weiteren Öffnung deines Herzens und zur Erweiterung deiner Fähigkeit wahrhaft fühlen zu können, runden den Weg ab, den du während des Workshops beschreitest. Du wirst unterschiedliche kraftvolle Energien und Potenziale in dir öffnen und zum Ende des Workshops lässt du dir vom InnenFeld zeigen, welche praktischen Schritte in deinem Alltag notwendig sind, um diese dort vollständig zu etablieren.</p>
<p class="abs copy" style="top:894px">Weitere Informationen zum Lesen im InnenFeld findest du <a>hier.</a></p>

<section class="abs times">
  <div class="times-head">Workshopzeiten</div>
  <div class="times-row"><span>1. Tag</span><span>15.00 – 18.30 Uhr</span></div>
  <div class="times-row"><span>2. – 4. Tag</span><span>09.00 – 18.30 Uhr</span></div>
  <div class="times-row"><span>5. Tag</span><span>09.00 – 13.00 Uhr</span></div>
</section>

<div class="abs social">
  <span><svg width="7" height="7" viewBox="0 0 10 10"><circle cx="5" cy="5" r="3.5" fill="none" stroke="#333" stroke-width="1"/></svg></span>
  <span><svg width="7" height="7" viewBox="0 0 10 10"><path d="M1 5 L9 1 L6 9 L5 5 Z" fill="none" stroke="#333" stroke-width="1"/></svg></span>
  <span><svg width="7" height="7" viewBox="0 0 10 10"><rect x="1.5" y="1.5" width="7" height="7" fill="none" stroke="#333" stroke-width="1"/></svg></span>
</div>

<nav class="abs footer-nav"><span>Impressum</span><span>Datenschutz</span><span>AGB</span><span>Kontakt</span></nav>
<div class="abs footer-line"></div>
<p class="abs rights">© 2022 All Rights Reserved</p>
</body>
</html>
```